Maple Vita App Landing Page

Looking for a landing page for our app at maplevitaco.example

Target Market(s)

Health care facilities

Industry/Entity Type

Healthcare

Number of Pages Required

1 page

```html
<!DOCTYPE html>
<html lang="en">
<head>
<meta charset="utf-8">
<title>Maple Vita – Covid-19 Screening</title>
<link href="https://fonts.googleapis.com/css2?family=Poppins:wght@300;400;500;600;700&family=Courier+Prime&display=swap" rel="stylesheet">
<style>
:root{
  --brand:#1479e8;
  --ink:#1d1f27;
  --muted:#8a8a8a;
  --body:#555a63;
  --sky-1:#5fd8f0;
  --sky-2:#1ea6ec;
  --sky-3:#0f6fe0;
  --teal:#14919b;
  --coral:#f2553b;
  --white:#ffffff;
}
*{margin:0;padding:0;box-sizing:border-box}
html,body{width:1200px;height:800px;overflow:hidden}
body{font-family:"Poppins",sans-serif;background:var(--white);position:relative}
.panel-left{position:absolute;left:0;top:0;width:539px;height:800px;background:var(--white)}
.panel-right{position:absolute;left:539px;top:0;width:661px;height:800px;overflow:hidden;
  background:linear-gradient(160deg,var(--sky-1) 0%,var(--sky-2) 45%,var(--sky-3) 100%)}
.blob{position:absolute;border-radius:50%}
.blob-a{left:120px;top:52px;width:72px;height:72px;background:radial-gradient(circle at 35% 35%,#4fd2f5,#1279e4)}
.blob-b{left:345px;top:82px;width:48px;height:48px;background:radial-gradient(circle at 35% 35%,#6fb4ec,#2a86dc)}
.blob-c{left:520px;top:-40px;width:220px;height:200px;background:radial-gradient(circle,#3b8fe8,#2a7ae0);opacity:.7;border-radius:45%}
.blob-d{left:-60px;top:520px;width:260px;height:260px;background:radial-gradient(circle,#1d86e6,#0f63d6);opacity:.7}
.blob-e{left:460px;top:520px;width:240px;height:240px;background:radial-gradient(circle,#2ad0f2,#12a7ea);opacity:.6}

.brand{position:absolute;left:66px;top:33px;display:flex;align-items:center;gap:10px;color:var(--brand);font-weight:600;font-size:26px;letter-spacing:-.3px}
.brand-dot{width:22px;height:22px;border-radius:50%;border:3px solid var(--brand)}

.nav{position:absolute;right:0;top:24px;display:flex;align-items:center;gap:36px;padding-right:66px;color:var(--white);font-size:13.5px;font-weight:500}
.nav-login{background:var(--white);color:var(--ink);padding:14px 31px;border-radius:0 24px 24px 24px;font-size:14.5px;font-weight:500}

.hero{position:absolute;left:65px;top:252px}
.hero-kicker{color:var(--muted);font-size:24px;font-weight:500}
.hero-title{color:var(--ink);font-size:50px;line-height:1.08;font-weight:300;margin-top:4px}
.hero-title strong{font-weight:700;display:block}
.hero-copy{color:var(--body);font-size:14.5px;line-height:1.4;margin-top:20px;width:390px}
.hero-cta{display:inline-block;margin-top:22px;width:210px;height:51px;line-height:51px;text-align:center;border-radius:26px 0 26px 26px;
  background:linear-gradient(90deg,#2cc3e8,#1479e8);color:var(--white);font-size:14px;font-weight:600;letter-spacing:.3px}

.copyright{position:absolute;left:66px;top:757px;font-size:13px;color:var(--ink)}

.social{position:absolute;left:1160px;top:341px;display:flex;flex-direction:column;gap:16px}
.social span{width:17px;height:17px;border-radius:50%;background:var(--white);display:block}

.phone{position:absolute;width:200px;height:400px;background:var(--white);border-radius:30px;transform:rotate(24deg);
  box-shadow:0 24px 40px rgba(10,40,90,.28);overflow:hidden}
.phone-head{height:78px;color:var(--white);text-align:center;padding-top:32px;position:relative}
.phone-head::before{content:"";position:absolute;left:80px;top:12px;width:34px;height:4px;border-radius:2px;background:var(--white)}
.phone-head h3{font-size:11px;font-weight:500;letter-spacing:.4px}
.phone-head small{display:block;font-size:5px;letter-spacing:.6px;opacity:.9}
.phone-head .back,.phone-head .close{position:absolute;top:36px;font-size:11px}
.phone-head .back{left:14px}.phone-head .close{right:14px}
.head-teal{background:var(--teal)}
.head-blue{background:var(--brand)}
.head-coral{background:var(--coral)}
.phone-body{padding:14px 18px;font-size:8px}

.phone-admin{left:470px;top:218px}
.mono{font-family:"Courier Prime",monospace;color:var(--teal);font-size:8.6px;line-height:1.15}
.mono h4{text-align:center;font-size:10px;margin-bottom:8px;color:#0d6c74}
.field{border-bottom:1px solid var(--teal);color:#5b8f92;font-size:6.5px;padding:6px 0 2px;margin-top:4px}
.sign{border:1px solid var(--teal);border-radius:3px;height:18px;margin-top:8px;font-size:5px;color:#5b8f92;padding:5px 4px}
.btn-done{margin:6px 0 0 auto;width:34px;height:14px;border-radius:3px;background:#7cc3c6;color:var(--white);font-size:5px;text-align:center;line-height:14px}

.phone-welcome{left:774px;top:134px}
.welcome-brand{text-align:center;color:var(--brand);font-weight:600;font-size:16px;margin-top:14px}
.welcome-tag{text-align:center;color:#4b9ae8;font-size:5.5px}
.welcome-art{margin:16px auto 0;width:150px;height:120px;border-radius:10px;background:linear-gradient(135deg,#cfe3fb,#e9f2fd)}
.bar-btn{margin:22px auto 0;width:150px;height:16px;border-radius:3px;background:var(--brand);color:var(--white);font-size:5.5px;line-height:16px;padding-left:8px;position:relative}
.bar-btn::after{content:"›";position:absolute;right:8px;top:0;font-size:8px}

.phone-visitor{left:896px;top:398px}
.ask{text-align:center;color:var(--brand);font-size:6.5px;margin-bottom:6px}
.roles{display:grid;grid-template-columns:1fr 1fr;gap:8px}
.role{height:42px;border:1px solid var(--brand);border-radius:3px;color:var(--brand);font-size:5.5px;letter-spacing:.6px;text-align:center;padding-top:8px}
.role i{display:block;width:12px;height:10px;margin:0 auto 5px;background:var(--brand);border-radius:2px}
.role.is-active{background:var(--brand);color:var(--white)}
.role.is-active i{background:var(--white)}
.select{margin-top:8px;border:1px solid var(--brand);border-radius:3px;height:18px;font-size:5.5px;color:var(--ink);padding:5px}
.next{margin-top:8px;height:16px;border-radius:3px;background:var(--brand);color:var(--white);font-size:5.5px;line-height:16px;padding-left:8px}

.phone-triage{left:686px;top:542px}
.triage-note{text-align:center;color:var(--coral);font-size:7px;line-height:1.3}
.label{text-align:center;color:var(--coral);font-size:7px;margin-top:12px}
.input{border:1px solid var(--coral);border-radius:3px;height:18px;margin-top:6px;font-size:5px;color:#777;padding:5px}
.next-coral{margin-top:14px;height:16px;border-radius:3px;background:var(--coral);color:var(--white);font-size:5.5px;line-height:16px;padding-left:8px}
</style>
</head>
<body>
<div class="panel-left"></div>
<div class="panel-right">
  <span class="blob blob-c"></span>
  <span class="blob blob-d"></span>
  <span class="blob blob-e"></span>
  <span class="blob blob-a"></span>
  <span class="blob blob-b"></span>
</div>

<header>
  <div class="brand"><span class="brand-dot"></span>MAPLE VITA</div>
  <nav class="nav">
    <span>WHY PAYMENT APP</span>
    <span>ABOUT US</span>
    <span>PRICES</span>
    <span class="nav-login">LOGIN</span>
  </nav>
</header>

<section class="hero">
  <p class="hero-kicker">Start your</p>
  <h1 class="hero-title">Covid-19<strong>Screening Now</strong></h1>
  <p class="hero-copy">Lorem ipsum dolor sit ametut labore et dolore Quis ipsum suspendisse ultrices</p>
  <a class="hero-cta">DOWNLOAD THE APP</a>
</section>

<p class="copyright">© COPYRIGHT 2020 ALL RIGHT RESERVED</p>

<div class="social" aria-label="Social links">
  <span role="img" aria-label="Social network link"></span>
  <span role="img" aria-label="Social network link"></span>
  <span role="img" aria-label="Social network link"></span>
  <span role="img" aria-label="Social network link"></span>
</div>

<div class="phone phone-admin">
  <div class="phone-head head-teal"><span class="back">‹</span><h3>COVID-19 ADMIN SCREEN</h3><small>ADMIN SCREEN · VENDOR EXCEPTION</small><span class="close">×</span></div>
  <div class="phone-body mono">
    <h4>Vendor Exception</h4>
    <p>In an effort to minimize exposure risk to all of our residents, we are restricting the vendors from entering the facility. Thank you for completing this screening process.</p>
    <p style="margin-top:6px">I, Name/Title ________, am employed by Entity ________, and request an essential visit for the following reason(s): Reason(s) ______ I am attesting that my visit is necessary and imminent in nature.</p>
    <div class="field">Entity Phone Number</div>
    <div class="field">Entity email</div>
    <div class="sign">Sign with initials</div>
    <div class="btn-done">Done</div>
  </div>
</div>

<div class="phone phone-welcome">
  <div class="phone-head head-blue"><h3>COVID-19 SCREENING</h3><small>SCREENING · WELCOME</small></div>
  <div class="phone-body">
    <div class="welcome-brand">MAPLE VITA</div>
    <div class="welcome-tag">Keeping you safe.</div>
    <div class="welcome-art" role="img" aria-label="Illustration of people walking with face masks"></div>
    <div class="bar-btn">Start your COVID-19 screening now</div>
  </div>
</div>

<div class="phone phone-visitor">
  <div class="phone-head head-blue"><span class="back">‹</span><h3>COVID-19 SCREENING</h3><small>SCREENING · STEP 1</small><span class="close">×</span></div>
  <div class="phone-body">
    <div class="ask">Who are you?</div>
    <div class="roles">
      <div class="role"><i></i>STAFF</div>
      <div class="role"><i></i>PROVIDER</div>
      <div class="role is-active"><i></i>VISITOR</div>
      <div class="role"><i></i>VENDOR</div>
    </div>
    <div class="ask" style="margin-top:10px">Which facility are you at?</div>
    <div class="select">Oak Row Clinic</div>
    <div class="next">Next</div>
  </div>
</div>

<div class="phone phone-triage">
  <div class="phone-head head-coral"><span class="back">‹</span><h3>COVID-19 TRIAGE</h3><small>TRIAGE · TEMPERATURE</small><span class="close">×</span></div>
  <div class="phone-body">
    <div class="triage-note">Please go to reception desk for a temperature reading</div>
    <div class="label">Temperature</div>
    <div class="input">98.6°F</div>
    <div class="label">Nurse ID</div>
    <div class="input">####</div>
    <div class="next-coral">Next</div>
  </div>
</div>
</body>
</html>
```